Frozen Yogurt Website

I need a new website based in Sydney Darling Harbour. Our products are:

Frozen Yogurt
Smoothies
Organic Acai Bowls / Smoothies

we have professional photos of gourmet fruit and toppings in high resolution
we have the logo
we just need a web designer

no ecommerce required. Just promotional website:

following pages are needed:

About Us
Contact Us
Frozen Yogurt
Toppings
Smoothies
Acai Bowls

examples of websites we like:
http://www.velmarokest.com
http://ourbrightpantrynook.com.au/
http://www.kalvu.com.au

any questions please feel free to ask

Target Market(s)

healthy and organic food lovers
Frozen yogurt / desert eaters
tourist in darling harbour

Industry/Entity Type

Promotional

Requirements
Should not have
• no ecommerce required

```html
<!DOCTYPE html>
<html lang="en">
<head>
<meta charset="utf-8">
<title>Yomira – authentic frozen yogurt</title>
<link rel="stylesheet" href="https://fonts.googleapis.com/css2?family=Open+Sans:wdth,wght@75,300;75,400&family=Fondamento&display=swap">
<style>
:root{
  --lime:#b3c11c;
  --slate:#2f3b45;
  --orange:#f26b1d;
  --ink:#2e3a44;
  --body-grey:#7a7a7a;
  --panel-grey:#efefef;
  --footer-black:#151515;
  --footer-grey:#5a5a5a;
  --photo-a:#cfcfcd;
  --photo-b:#b9b9b6;
}
*{margin:0;padding:0;box-sizing:border-box}
html,body{width:1200px;height:826px;overflow:hidden;background:#fff}
body{position:relative;font-family:Arial,Helvetica,sans-serif}
.cond{font-family:"Open Sans",sans-serif;font-stretch:75%}

.top-rule{position:absolute;left:0;top:0;width:1200px;height:5px;background:var(--lime)}

.site-header{position:absolute;left:0;top:5px;width:1200px;height:83px}
.brand{position:absolute;left:192px;top:16px;display:flex;flex-direction:column}
.brand-name{font-family:"Open Sans",sans-serif;font-stretch:75%;font-weight:400;font-size:52px;line-height:46px;color:var(--ink);letter-spacing:-1px}
.brand-sub{font-family:"Open Sans",sans-serif;font-stretch:75%;font-size:12px;color:var(--orange);margin-left:30px;margin-top:2px}

.main-nav{position:absolute;left:360px;top:12px;display:flex;gap:4px}
.main-nav a{display:flex;align-items:center;justify-content:center;width:91px;height:61px;background:var(--slate);color:#fff;text-decoration:none;font-family:"Open Sans",sans-serif;font-stretch:75%;font-size:16px;font-weight:300}
.main-nav a.home{width:77px;background:none;color:var(--ink)}

.hero-band{position:absolute;left:0;top:88px;width:1200px;height:348px;background:#fff;box-shadow:0 4px 6px rgba(0,0,0,.35);border-top:1px solid #e4e4e4}
.hero-photo{position:absolute;left:192px;top:12px;width:817px;height:324px;background:linear-gradient(135deg,var(--photo-a),var(--photo-b))}
.hero-caption{position:absolute;left:0;top:231px;width:400px;height:65px;background:rgba(70,70,70,.78);color:#fff;font-size:15px;font-weight:300;padding:20px 0 0 128px}
.hero-arrow{position:absolute;top:148px;width:30px;height:30px}
.hero-arrow.prev{left:6px}
.hero-arrow.next{right:6px}

.features{position:absolute;left:192px;top:454px;display:flex;gap:29px}
.feature{width:253px}
.feature h2{font-family:"Open Sans",sans-serif;font-stretch:75%;font-weight:300;font-size:32px;line-height:36px;color:#222;border-left:7px solid var(--orange);border-bottom:2px solid var(--orange);padding-left:6px}
.feature p{margin-top:16px;font-size:14px;line-height:16.5px;color:var(--body-grey)}

.motto{position:absolute;left:192px;top:623px;width:817px;height:61px;background:var(--panel-grey);display:flex;align-items:center;justify-content:center;font-family:"Fondamento",serif;font-size:15.5px;color:var(--orange);white-space:nowrap}

.site-footer{position:absolute;left:0;top:711px;width:1200px;height:97px;background:var(--footer-black)}
.footer-links{position:absolute;left:196px;top:35px;width:270px;text-align:center;color:#fff;font-size:13px;line-height:15px}
.footer-name{position:absolute;left:544px;top:35px;width:82px;text-align:center;font-family:"Open Sans",sans-serif;font-stretch:75%;font-size:24px;line-height:28px;color:var(--footer-grey)}
.social{position:absolute;left:802px;top:9px;display:flex;gap:14px}
.social span{width:30px;height:30px;border-radius:5px;background:#3a6ea5}
.social span:nth-child(3){background:#2f86b8}
.social span:nth-child(4){background:#2aa7d6}
.social span:nth-child(5){background:#e8e8e8}
.contact{position:absolute;left:803px;top:50px;width:200px;text-align:center;color:var(--footer-grey);font-size:13px;line-height:17px}

.copyright{position:absolute;left:0;top:808px;width:1200px;height:18px;background:var(--slate);color:#fff;font-size:13px;text-align:center;padding-top:8px;line-height:13px}
</style>
</head>
<body>
<div class="top-rule"></div>

<header class="site-header">
  <div class="brand">
    <span class="brand-name">yomira</span>
    <span class="brand-sub">authentic frozen yogurt</span>
  </div>
  <nav class="main-nav">
    <a class="home" href="#">Home</a>
    <a href="#">About Us</a>
    <a href="#">Contact Us</a>
    <a href="#">Frozen Yogurt</a>
    <a href="#">Toppings</a>
    <a href="#">Smoothies</a>
    <a href="#">Acai Bowls</a>
  </nav>
</header>

<section class="hero-band">
  <div class="hero-photo" role="img" aria-label="Overhead photo of peaches, grapefruit halves, coconut-dusted treats and green leaves scattered on grey concrete">
    <div class="hero-caption cond">Lorem ipsum dolor sit amet.3</div>
    <svg class="hero-arrow prev" viewBox="0 0 30 30"><circle cx="15" cy="15" r="15" fill="rgba(255,255,255,.35)"/><path d="M19 5 L9 15 L19 25" fill="none" stroke="#9a9a9a" stroke-width="5"/></svg>
    <svg class="hero-arrow next" viewBox="0 0 30 30"><circle cx="15" cy="15" r="15" fill="rgba(255,255,255,.35)"/><path d="M11 5 L21 15 L11 25" fill="none" stroke="#9a9a9a" stroke-width="5"/></svg>
  </div>
</section>

<section class="features">
  <article class="feature">
    <h2>Delicious</h2>
    <p>Our signature frozen yogurt is authentic. Using the freshest organic low fat milk, and fresh organic low fat yogurt. Giving you the best tasting yogurt experience</p>
  </article>
  <article class="feature">
    <h2>Nutritious</h2>
    <p>98% fat free, live and active cultures with probiotics so only the best are being consumed.</p>
  </article>
  <article class="feature">
    <h2>Conscious</h2>
    <p>Our Acai range are organic and fair trade making sure we not only nourish our bodies with the best ingredients but we also conscious of people who have made our product are being looked after too.</p>
  </article>
</section>

<div class="motto">Yomira - yo.mir.a | noun a healthy and delicious frozen yogurt treat that sends your taste buds into a state of euphoria</div>

<footer class="site-footer">
  <div class="footer-links">About Us &nbsp;| &nbsp;Contact Us &nbsp;| &nbsp;Frozen Yogurt<br>Toppings &nbsp;| &nbsp;Smoothies &nbsp;| &nbsp;Acai Bowls</div>
  <div class="footer-name">yomira</div>
  <div class="social" aria-label="Social links"><span></span><span></span><span></span><span></span><span></span></div>
  <div class="contact">contact@yomira.com<br>www.yomira.com</div>
</footer>
<div class="copyright">Copyright © 2013 Yomira. All Rights Reserved</div>
</body>
</html>
```